Cognitive therapist.

I am a therapist and my main work is with clients who have depression and anxiety disorders.

I need something reasonably plain. Cognitive therapy is a very pragmatic approach to dealing with problems, so it isn't new agey (no offence to new age therapies at all)

Hi everyone, I am currently looking at a particular design that I will most likely go with. Cheers, Lyn

Lyn Marchet
Cognitive Therapist
BA, PG Dip Mental Health,
PG Dip Cog Beh Therapy
MKRPG

The Quillan Rooms,
Level One
47 Harwick Parade
Cnr Drayfield St & Harwick Parade
P O Box 38 215
WELLINGTON 6287

Phone: 027 463 2851 Email: lmarchet@quorvane.co.nz

www.lynmarchet.co.nz

• No illustration, or colour. not old style fonts.

```html
<!DOCTYPE html>
<html lang="en">
<head>
<meta charset="utf-8">
<title>Lyn Marchet – Cognitive Therapy business card</title>
<link rel="stylesheet" href="https://fonts.googleapis.com/css2?family=Exo+2:wght@400;500&family=Open+Sans:wght@400&display=swap">
<style>
  :root {
    --page-bg: #e9e9ea;
    --card-white: #ffffff;
    --brand-blue: #00adef;
    --band-grey: #6d6e71;
    --ink-dark: #2b2b2d;
    --ink-muted: #5a5b5e;
    --ink-light: #ffffff;
    --cell-rule: rgba(0, 0, 0, 0.22);
  }
  * { margin: 0; padding: 0; box-sizing: border-box; }
  html, body {
    width: 1200px;
    height: 939px;
    overflow: hidden;
    background: var(--page-bg);
  }
  .canvas {
    position: relative;
    width: 1200px;
    height: 939px;
  }
  .card {
    position: absolute;
    left: 120px;
    top: 195px;
    width: 960px;
    height: 549px;
    background: var(--card-white);
    overflow: hidden;
    box-shadow: 0 10px 30px rgba(0, 0, 0, 0.18);
  }
  .card__band {
    position: absolute;
    left: 0;
    right: 0;
    top: 330px;
    bottom: 0;
    background: var(--band-grey);
  }
  .identity {
    position: absolute;
    left: 56px;
    top: 96px;
    width: 440px;
    color: var(--ink-dark);
    font-family: "Exo 2", sans-serif;
  }
  .identity__name {
    font-size: 42px;
    font-weight: 500;
    letter-spacing: 1px;
    line-height: 1.1;
  }
  .identity__role {
    margin-top: 4px;
    margin-left: 8px;
    font-size: 28px;
    font-weight: 400;
    letter-spacing: 1px;
    line-height: 1.2;
  }
  .identity__credentials {
    margin-top: 10px;
    margin-left: 8px;
    font-family: "Open Sans", sans-serif;
    font-size: 14px;
    line-height: 1.45;
    color: var(--ink-muted);
  }
  .practice {
    position: absolute;
    left: 540px;
    top: 70px;
    width: 390px;
  }
  .practice__name {
    color: var(--brand-blue);
    font-family: "Open Sans", sans-serif;
    font-size: 40px;
    font-weight: 400;
    line-height: 1.3;
  }
  .practice__address {
    margin-top: 10px;
    font-family: "Open Sans", sans-serif;
    font-style: normal;
    font-size: 14px;
    line-height: 1.45;
    color: var(--ink-muted);
  }
  .contacts {
    position: absolute;
    left: 106px;
    top: 272px;
    width: 825px;
    height: 228px;
    display: flex;
    background: var(--brand-blue);
  }
  .contact {
    flex: 1;
    position: relative;
    border-right: 1px solid var(--cell-rule);
    color: var(--ink-light);
    font-family: "Open Sans", sans-serif;
    font-size: 19px;
    text-align: center;
  }
  .contact:last-child { border-right: none; }
  .contact__icon {
    position: absolute;
    left: 50%;
    top: 44px;
    width: 30px;
    height: 30px;
    transform: translateX(-50%);
  }
  .contact__text {
    position: absolute;
    left: 0;
    right: 0;
    top: 140px;
  }
</style>
</head>
<body>
<main class="canvas">
  <article class="card">
    <div class="card__band"></div>

    <header class="identity">
      <h1 class="identity__name">Lyn Marchet</h1>
      <p class="identity__role">Cognitive Therapist</p>
      <p class="identity__credentials">BA, PG Dip Mental Health,<br>PG Dip Cog Beh Therapy · MKRPG</p>
    </header>

    <section class="practice">
      <p class="practice__name">Cognitive Therapy</p>
      <address class="practice__address">
        The Quillan Rooms, Level One, 47 Harwick Parade<br>
        Cnr Drayfield St &amp; Harwick Parade<br>
        P O Box 38 215, WELLINGTON 6287
      </address>
    </section>

    <section class="contacts">
      <div class="contact contact--email">
        <svg class="contact__icon" viewBox="0 0 30 30" aria-hidden="true">
          <rect x="3" y="7" width="24" height="16" fill="#fff"/>
          <path d="M3 7 L15 17 L27 7" fill="none" stroke="#00adef" stroke-width="2"/>
        </svg>
        <p class="contact__text">lmarchet@quorvane.co.nz</p>
      </div>
      <div class="contact contact--phone">
        <svg class="contact__icon" viewBox="0 0 30 30" aria-hidden="true">
          <path d="M9 3 L13 3 L14 10 L11 12 C12.5 16 14 18 18 20 L20 17 L27 18 L27 22 C27 25 24 27 21 27 C12 26 4 18 3 9 C3 6 5 3 9 3 Z" fill="#fff"/>
        </svg>
        <p class="contact__text">027 463 2851</p>
      </div>
      <div class="contact contact--web">
        <svg class="contact__icon" viewBox="0 0 30 30" aria-hidden="true">
          <g fill="none" stroke="#fff" stroke-width="2">
            <circle cx="15" cy="15" r="12"/>
            <ellipse cx="15" cy="15" rx="5" ry="12"/>
            <line x1="3" y1="15" x2="27" y2="15"/>
            <path d="M5 9 H25 M5 21 H25"/>
          </g>
        </svg>
        <p class="contact__text">www.lynmarchet.co.nz</p>
      </div>
    </section>
  </article>
</main>
</body>
</html>
```